Harbouring Dawn Rituals creates individual, personalised ceremonies to celebrate weddings, naming days,coming of age, significant age, divorce and final resting rites. Ceremonies and meaningful rituals are created in collaboration with the individual to reflect their hopes and desires, how they will/have embrace/d their lives. The final design should have the logo (purple) on a white/silver background on the right hand side of the card. Name of business and contact details in red on a black background on the left
Updates

Hi All, have only just realised I have paid for a double sided card, yep, a newbie! Sorry to set the cat amongst the pigeons but could we put 'creating...... etc' on the back?

Target Market(s)

Couples marrying, renewing of vows, baby naming days, coming of age, significant age, divorce, funeral ceremonies. The target market predominantly will be couples marrying.

Industry/Entity Type

Business

Contact Information for Business Card

Harbouring Dawn Rituals, Doriane Whitcombe, 0428-735902 harbouringdawnrituals1@examplemail.test
"Shaping singular, tailored rituals harbouring dawn"

Font styles to use
Script

Colors
eb1f27
6b449b
f3f0f8

Requirements
Must have
• On initial entry, and now, the logo was not displayed in full - the bottom part was cut off - this needs to be in it's entirety. Colours as previously specified are non-negotiable. Font and placement of characters will be assessed as produced.
Should not have
• Telephone symbol, call us, director,grammatical symbols ( : )

```html
<!DOCTYPE html>
<html lang="en">
<head>
<meta charset="utf-8">
<title>Harbouring Dawn Rituals – Business Card</title>
<link rel="stylesheet" href="https://fonts.googleapis.com/css2?family=Fondamento&display=swap">
<style>
  :root {
    --backdrop: #e7e4e1;
    --card-black: #050505;
    --card-charcoal: #2b2b2b;
    --band-dark: #1c1c1c;
    --band-mid: #3a3a3a;
    --band-light: #555555;
    --silver-top: #ffffff;
    --silver-bottom: #d6d0d0;
    --contact-red: #eb1f27;
    --brand-purple: #6b449b;
    --brand-lilac: #f3f0f8;
  }
  * { margin: 0; padding: 0; box-sizing: border-box; }
  html, body {
    width: 1200px;
    height: 1200px;
    overflow: hidden;
    background: var(--backdrop);
  }
  .canvas {
    position: relative;
    width: 1200px;
    height: 1200px;
  }
  .business-card {
    position: absolute;
    left: 25px;
    top: 246px;
    width: 1150px;
    height: 708px;
    overflow: hidden;
    background: radial-gradient(ellipse at 30% 45%, var(--card-charcoal) 0%, var(--card-black) 70%);
    box-shadow: 0 10px 30px rgba(0,0,0,0.25);
  }
  .card-shapes {
    position: absolute;
    inset: 0;
  }
  .contact-block {
    position: absolute;
    left: 72px;
    top: 86px;
    font-family: "Fondamento", cursive;
    color: var(--contact-red);
  }
  .contact-name {
    font-size: 40px;
    line-height: 1.2;
    letter-spacing: 0.5px;
  }
  .contact-phone {
    margin-top: 4px;
    font-size: 36px;
    line-height: 1.2;
  }
  .contact-email {
    margin-top: 6px;
    font-size: 23px;
    line-height: 1.3;
  }
  .brand-block {
    position: absolute;
    left: 650px;
    top: 0;
    width: 500px;
    display: flex;
    flex-direction: column;
    align-items: center;
  }
  .brand-dot {
    width: 160px;
    height: 160px;
    border-radius: 50%;
    background: var(--brand-lilac);
    margin-top: 145px;
    margin-bottom: 130px;
  }
  .brand-name {
    font-family: "Fondamento", cursive;
    color: var(--brand-purple);
    font-size: 38px;
    line-height: 1.4;
    text-align: center;
    text-transform: uppercase;
    letter-spacing: 1px;
    white-space: nowrap;
  }
</style>
</head>
<body>
<div class="canvas">
  <section class="business-card">
    <svg class="card-shapes" width="1150" height="708" viewBox="0 0 1150 708">
      <defs>
        <linearGradient id="silverFace" x1="0" y1="0" x2="0" y2="1">
          <stop offset="0" stop-color="#ffffff"/>
          <stop offset="1" stop-color="#d6d0d0"/>
        </linearGradient>
      </defs>
      <path class="wave-band wave-band--dark" d="M690 0 C560 110 520 230 530 400 C540 560 555 640 500 708 L1150 708 L1150 0 Z" fill="var(--band-dark)"/>
      <path class="wave-band wave-band--mid" d="M715 0 C585 115 555 240 565 400 C575 560 590 640 535 708 L1150 708 L1150 0 Z" fill="var(--band-mid)"/>
      <path class="wave-band wave-band--light" d="M735 0 C610 118 585 245 592 400 C600 560 615 640 562 708 L1150 708 L1150 0 Z" fill="var(--band-light)"/>
      <path class="silver-face" d="M750 0 C630 120 605 250 610 400 C615 560 630 640 580 708 L1150 708 L1150 0 Z" fill="url(#silverFace)"/>
    </svg>

    <div class="contact-block">
      <p class="contact-name">Doriane Whitcombe</p>
      <p class="contact-phone">0428-735902</p>
      <p class="contact-email">harbouringdawnrituals1@examplemail.test</p>
    </div>

    <div class="brand-block">
      <div class="brand-dot"></div>
      <p class="brand-name">Harbouring Dawn<br>Rituals</p>
    </div>
  </section>
</div>
</body>
</html>
```